wine bottle label design

My girlfriend and I are getting married. We are sending out invitations, in a wine bottle. For that we need a label on the bottle.
Our names are Marlene & Henrik. We would like the C and K to somehow play a bigger part in the logo.
Also maybe with an Illustration (best if made as a drawing resembling the church we are getting married in) https://www.sangfolket.dk/index.php/kalender/83-uncategorised/148-gospelgudstjeneste-i-tarnholm-kirke.html

Logo Text

Bryllup den 27 april 2019, kl. 14:00 i Tarnholm Kirke

Font styles to use
Decorative

```html
<!DOCTYPE html>
<html lang="da">
<head>
<meta charset="utf-8">
<title>Bryllupsetiket – Henrik &amp; Marlene</title>
<link rel="stylesheet" href="https://fonts.googleapis.com/css2?family=Bodoni+Moda:wght@500&family=Great+Vibes&family=Oranienbaum&display=swap">
<style>
  :root {
    --blush: #f0dad4;
    --ink: #0c0b0b;
    --pale-text: #f2ddd6;
    --glow: #fdf6f3;
    --page: #ffffff;
  }
  html, body {
    margin: 0;
    padding: 0;
    width: 1111px;
    height: 1200px;
    overflow: hidden;
    background: var(--page);
  }
  .canvas {
    position: relative;
    width: 1111px;
    height: 1200px;
  }
  .label {
    position: absolute;
    left: 55px;
    top: 67px;
    width: 1000px;
    height: 1065px;
    background: var(--blush);
    overflow: hidden;
  }
  .label__band {
    position: absolute;
    left: 0;
    top: 719px;
    width: 100%;
    height: 346px;
    background: var(--ink);
  }
  .monogram-frame {
    position: absolute;
    left: 222px;
    top: 68px;
    width: 536px;
    height: 431px;
    border-radius: 50%;
    background: radial-gradient(ellipse at center, var(--glow) 0%, rgba(253,246,243,0.6) 35%, rgba(240,218,212,0) 70%);
  }
  .monogram {
    position: absolute;
    left: 0;
    top: 165px;
    width: 980px;
    margin: 0;
    text-align: center;
    font-family: "Bodoni Moda", "Didot", serif;
    font-weight: 500;
    font-size: 230px;
    line-height: 1;
    letter-spacing: 4px;
    color: var(--ink);
  }
  .couple {
    position: absolute;
    left: 90px;
    top: 570px;
    width: 640px;
    margin: 0;
    text-align: center;
    font-family: "Great Vibes", cursive;
    font-weight: 400;
    font-size: 74px;
    line-height: 1;
    word-spacing: 8px;
    color: var(--ink);
  }
  .details {
    position: absolute;
    left: 170px;
    top: 840px;
    margin: 0;
    font-family: "Oranienbaum", "Bodoni Moda", serif;
    font-size: 42px;
    line-height: 72px;
    color: var(--pale-text);
    letter-spacing: 0.5px;
  }
  .church-illustration {
    position: absolute;
    left: 765px;
    top: 434px;
    width: 235px;
    height: 631px;
  }
</style>
</head>
<body>
  <main class="canvas">
    <section class="label">
      <div class="label__band"></div>
      <div class="monogram-frame" role="img" aria-label="Ornamental swirl frame surrounding the monogram"></div>
      <h1 class="monogram">HM</h1>
      <p class="couple">Henrik &amp; Marlene</p>
      <p class="details">Bryllup den 27 april 2019,<br>kl.&nbsp; 14:00&nbsp; i&nbsp; Tarnholm&nbsp; Kirke</p>
      <svg class="church-illustration" viewBox="0 0 235 631" role="img" aria-label="Line drawing of Tarnholm Kirke with its clock tower">
        <defs>
          <linearGradient id="churchTone" x1="0" y1="0" x2="0" y2="1">
            <stop offset="0" stop-color="#d9c4be"/>
            <stop offset="0.45" stop-color="#6e6462"/>
            <stop offset="1" stop-color="#2a2828"/>
          </linearGradient>
        </defs>
        <rect x="0" y="0" width="235" height="631" fill="url(#churchTone)" opacity="0.55"/>
      </svg>
    </section>
  </main>
</body>
</html>
```